Company or website name
- Marla Quist Design & Decor
- Passionate about wedding floral design and decor. Events I create are timeless, classic and elegant, customized 100% to the brides’ desires. Inspiring them with a vision of what is possible & asking them to step inside it and see it for themselves

```html
<!DOCTYPE html>
<html lang="en">
<head>
<meta charset="utf-8">
<title>Marla Quist Design &amp; Decor — Stationery</title>
<link rel="stylesheet" href="https://fonts.googleapis.com/css2?family=EB+Garamond:wght@400&family=Lato:wght@300&display=swap">
<style>
  :root {
    --paper: #ffffff;
    --blush: #f6e4eb;
    --rose: #d35a89;
    --rose-text: #d0799d;
    --edge: rgba(0, 0, 0, 0.18);
  }
  html, body {
    margin: 0;
    padding: 0;
    overflow: hidden;
    background: var(--paper);
  }
  .canvas {
    position: relative;
    width: 1091px;
    height: 1200px;
    overflow: hidden;
    background: var(--paper);
  }

  /* Letterhead */
  .letterhead {
    position: absolute;
    left: 225px;
    top: 94px;
    width: 822px;
    height: 1064px;
    background: var(--paper);
    box-shadow: 2px 2px 4px var(--edge);
    overflow: hidden;
  }
  .letterhead__shapes {
    position: absolute;
    inset: 0;
  }
  .letterhead__contact {
    position: absolute;
    left: 785px;
    top: 804px;
    transform: rotate(-90deg);
    transform-origin: 0 0;
    white-space: nowrap;
    font-family: "Lato", sans-serif;
    font-weight: 300;
    font-size: 14.5px;
    letter-spacing: 0.2px;
    color: var(--rose-text);
  }
  .brand {
    position: absolute;
    display: flex;
    align-items: center;
  }
  .brand__dot {
    border-radius: 50%;
    background: var(--rose);
    flex: none;
  }
  .brand__name {
    font-family: "EB Garamond", serif;
    font-weight: 400;
    color: var(--rose);
    line-height: 1.05;
  }
  .letterhead .brand {
    left: 126px;
    top: 810px;
    gap: 20px;
  }
  .letterhead .brand__dot { width: 130px; height: 130px; }
  .letterhead .brand__name { font-size: 36px; margin-top: 120px; }

  /* Business card */
  .business-card {
    position: absolute;
    left: 78px;
    top: 290px;
    width: 198px;
    height: 336px;
    background: var(--paper);
    box-shadow: 2px 2px 4px var(--edge);
    overflow: hidden;
  }
  .business-card__circle {
    position: absolute;
    left: 49px;
    top: 66px;
    width: 154px;
    height: 154px;
    border-radius: 50%;
    background: var(--blush);
  }
  .business-card__details {
    position: absolute;
    right: 24px;
    top: 21px;
    text-align: right;
    font-family: "Lato", sans-serif;
    font-weight: 300;
    color: var(--rose-text);
  }
  .business-card__person {
    font-size: 11.5px;
    margin: 0 0 10px;
  }
  .business-card__line {
    font-size: 9px;
    line-height: 13px;
    margin: 0;
  }
  .business-card .brand {
    left: 35px;
    top: 237px;
    flex-direction: column;
    align-items: flex-start;
    gap: 6px;
  }
  .business-card .brand__dot { width: 52px; height: 52px; }
  .business-card .brand__name { font-size: 15px; margin-left: -6px; }
</style>
</head>
<body>
<main class="canvas">

  <section class="letterhead" aria-label="Letterhead">
    <svg class="letterhead__shapes" width="822" height="1064" viewBox="0 0 822 1064" aria-hidden="true">
      <circle cx="227" cy="294" r="397" fill="var(--blush)"/>
      <circle cx="769" cy="900" r="235" fill="var(--blush)"/>
    </svg>

    <p class="letterhead__contact">Marla Quist Design &amp; Decor . 123 Street Address . City, State 12345 . 222.555.1212 . address@email.com</p>

    <div class="brand">
      <span class="brand__dot"></span>
      <span class="brand__name">Marla Quist<br>design &amp; decor</span>
    </div>
  </section>

  <section class="business-card" aria-label="Business card">
    <span class="business-card__circle"></span>
    <div class="business-card__details">
      <p class="business-card__person">Marla Quist</p>
      <p class="business-card__line">123 Street Address</p>
      <p class="business-card__line">City, State 12345</p>
      <p class="business-card__line">222.555.1212</p>
      <p class="business-card__line">address@email.com</p>
    </div>
    <div class="brand">
      <span class="brand__dot"></span>
      <span class="brand__name">Marla Quist<br>design &amp; decor</span>
    </div>
  </section>

</main>
</body>
</html>
```